Lena Corvell Business Card

I need a business card that reflects my current website: itslenacorvell.example and screenshot attached. If we keep the color scheme of the site and sample card below that would be ideal. The business card should include the information on the attached sample cards.

Industry/Entity Type

Business

```html
<!DOCTYPE html>
<html lang="en">
<head>
<meta charset="utf-8">
<title>Lena Corvell Business Card</title>
<link rel="stylesheet" href="https://fonts.googleapis.com/css2?family=Didact+Gothic&display=swap">
<style>
  :root {
    --backdrop: #2a2a2a;
    --card-white: #f4f4f4;
    --lettering-tone: #dcdcdc;
    --teal-top: #00cbbd;
    --teal-bottom: #00b3a6;
    --card-text: #e8fbf9;
    --icon-fill: #d6f4f1;
  }
  * { box-sizing: border-box; margin: 0; padding: 0; }
  html, body { width: 1200px; height: 900px; overflow: hidden; }
  body {
    background: var(--backdrop);
    font-family: "Didact Gothic", "Century Gothic", sans-serif;
    position: relative;
  }
  .card {
    position: absolute;
    left: 300px;
    width: 600px;
    height: 343px;
    border-radius: 4px;
  }
  .card-back {
    top: 100px;
    background: var(--card-white);
  }
  .signature-mark {
    position: absolute;
    left: 150px;
    top: 120px;
    width: 320px;
    height: 110px;
    background: var(--lettering-tone);
    border-radius: 6px;
  }
  .card-front {
    top: 470px;
    background: linear-gradient(160deg, var(--teal-top), var(--teal-bottom));
    color: var(--card-text);
  }
  .holder-name {
    position: absolute;
    right: 36px;
    top: 44px;
    font-size: 36px;
    letter-spacing: 1px;
    text-transform: uppercase;
    font-weight: 400;
  }
  .holder-roles {
    position: absolute;
    right: 36px;
    top: 100px;
    font-size: 13px;
    letter-spacing: 0.5px;
  }
  .contact-list {
    position: absolute;
    left: 36px;
    bottom: 34px;
    list-style: none;
    font-size: 15px;
    line-height: 22px;
  }
  .contact-item {
    display: flex;
    align-items: center;
    gap: 8px;
  }
  .contact-icon { width: 15px; height: 15px; flex: none; }
  .contact-icon * { fill: var(--icon-fill); }
  .contact-icon .stroke { fill: none; stroke: var(--teal-bottom); stroke-width: 1.4; }
</style>
</head>
<body>
  <section class="card card-back">
    <div class="signature-mark" role="img" aria-label="Hand-lettered signature reading 'i am Lena Corvell' in black brush script"></div>
  </section>

  <section class="card card-front">
    <h1 class="holder-name">Lena Corvell</h1>
    <p class="holder-roles">Brand Curator · Digital Storyteller · Social Entrpreneur</p>
    <ul class="contact-list">
      <li class="contact-item">
        <svg class="contact-icon" viewBox="0 0 16 16" aria-hidden="true"><circle cx="8" cy="8" r="8"/><path class="stroke" d="M5.5 4.5c0 4 2 6 6 6"/></svg>
        555.014.2273
      </li>
      <li class="contact-item">
        <svg class="contact-icon" viewBox="0 0 16 16" aria-hidden="true"><circle cx="8" cy="8" r="8"/><rect class="stroke" x="4" y="5.5" width="8" height="5.5"/><path class="stroke" d="M4 5.5l4 3 4-3"/></svg>
        me@lenacorvell.example
      </li>
      <li class="contact-item">
        <svg class="contact-icon" viewBox="0 0 16 16" aria-hidden="true"><circle cx="8" cy="8" r="8"/><circle class="stroke" cx="8" cy="8" r="4.5"/><path class="stroke" d="M3.5 8h9M8 3.5c-2 2.5-2 6.5 0 9M8 3.5c2 2.5 2 6.5 0 9"/></svg>
        www.itslenacorvell.example
      </li>
      <li class="contact-item">
        <svg class="contact-icon" viewBox="0 0 16 16" aria-hidden="true"><circle cx="8" cy="8" r="7"/></svg>
        @itslenacorvell
      </li>
    </ul>
  </section>
</body>
</html>
```